HOLLOWPINE SPIRITS WEBSITE

HOLLOWPINE SPIRITS WHOLESALES ALCOHOL (WHISKY VODKA AND HELPS CREATES BOTTLING/BRANDING FOR PEOPLE WANTING LAUNCH THERE OWN BRANDS OF ALCOHOL

Colors

Designer to choose colors to be used in the design.

```html
<!DOCTYPE html>
<html lang="en">
<head>
<meta charset="utf-8">
<title>Hollowpine Spirits</title>
<link rel="stylesheet" href="https://fonts.googleapis.com/css2?family=EB+Garamond:wght@400;500&display=swap">
<style>
  :root {
    --bg-dark: #141212;
    --bg-footer: #1e1a1a;
    --hero-deep: #1c1614;
    --hero-copper: #6b3f2c;
    --hero-warm: #3a2620;
    --gold: #c9a23a;
    --text: #f3eee8;
    --line: #e9e4de;
    --card: #221d1b;
  }
  * { margin: 0; padding: 0; box-sizing: border-box; }
  html, body { width: 894px; height: 1200px; overflow: hidden; background: var(--bg-dark); }
  body { position: relative; font-family: "EB Garamond", Georgia, serif; color: var(--text); }

  .hero-photo {
    position: absolute; left: 0; top: 0; width: 894px; height: 503px;
    background:
      radial-gradient(ellipse 180px 260px at 470px 300px, rgba(140,80,55,.55), transparent 70%),
      radial-gradient(ellipse 160px 110px at 150px 400px, rgba(120,70,50,.5), transparent 70%),
      radial-gradient(ellipse 120px 200px at 780px 200px, rgba(90,55,45,.45), transparent 70%),
      linear-gradient(180deg, var(--hero-deep) 0%, var(--hero-warm) 60%, #2a2220 100%);
  }
  .brand-mark {
    position: absolute; left: 25px; top: 20px;
    display: flex; align-items: center; gap: 5px;
    font-size: 10px; letter-spacing: .08em; color: var(--text); font-weight: 500;
  }
  .brand-mark .square { width: 9px; height: 9px; background: var(--gold); }

  .nav a {
    position: absolute; top: 17px; height: 21px;
    border: 1px solid var(--line); color: var(--text);
    font-size: 8px; letter-spacing: .03em; text-decoration: none;
    display: flex; align-items: center; justify-content: center;
  }

  .hero-title {
    position: absolute; left: 0; width: 894px; top: 166px;
    text-align: center; font-size: 56px; font-weight: 500; letter-spacing: .01em;
  }
  .hero-rule { position: absolute; left: 301px; top: 248px; width: 292px; height: 1px; background: var(--gold); }
  .hero-tagline { position: absolute; left: 0; width: 894px; top: 267px; text-align: center; font-size: 15px; }

  .bottle-photo {
    position: absolute; left: 405px; top: 430px; width: 445px; height: 505px;
    background: radial-gradient(ellipse 150px 240px at 55% 50%, rgba(150,80,45,.55), rgba(40,20,15,.35) 60%, transparent 80%);
  }

  .intro-frame { position: absolute; left: 253px; top: 419px; width: 384px; height: 163px; border: 1px solid var(--line); }
  .intro-card {
    position: absolute; left: 265px; top: 431px; width: 358px; height: 135px;
    border: 1px solid var(--gold); background: var(--card);
    padding: 23px 22px 0; text-align: center; font-size: 12px; line-height: 14px;
  }
  .intro-card p + p { margin-top: 14px; }

  .about-title { position: absolute; left: 50px; top: 548px; font-size: 24px; font-weight: 500; letter-spacing: .02em; }
  .about-rule { position: absolute; left: 76px; top: 581px; width: 37px; height: 1px; background: var(--gold); }
  .about-copy { position: absolute; left: 50px; top: 697px; width: 305px; font-size: 12.3px; line-height: 14px; }
  .about-copy p + p { margin-top: 14px; }

  .footer { position: absolute; left: 0; top: 998px; width: 894px; height: 202px; background: var(--bg-footer); }
  .footer-brand {
    position: absolute; left: 115px; top: 62px;
    display: flex; align-items: center; gap: 8px;
    font-size: 20px; font-weight: 500; letter-spacing: .06em;
  }
  .footer-brand .square { width: 16px; height: 16px; background: var(--gold); }
  .footer-tagline { position: absolute; left: 118px; top: 126px; width: 220px; font-size: 11px; line-height: 14px; }
  .footer-divider { position: absolute; left: 447px; top: 38px; width: 1px; height: 122px; background: var(--line); }
  .contact-item { position: absolute; left: 543px; display: flex; gap: 8px; font-size: 15px; line-height: 19px; }
  .contact-item svg { flex: none; margin-top: 2px; }
</style>
</head>
<body>
  <div class="hero-photo" role="img" aria-label="Dim distillery interior with copper pot still and oak barrels"></div>

  <div class="brand-mark"><span class="square"></span>HOLLOWPINE SPIRITS</div>

  <nav class="nav">
    <a href="#" style="left:274px;width:50px">HOME</a>
    <a href="#" style="left:359px;width:68px">WHOLESALE</a>
    <a href="#" style="left:465px;width:57px">SERVICES</a>
    <a href="#" style="left:559px;width:57px">CONTACT</a>
  </nav>

  <h1 class="hero-title">Welcome to Hollowpine</h1>
  <div class="hero-rule"></div>
  <p class="hero-tagline">Turn your next drink idea into a reality and share your product with the world.</p>

  <div class="bottle-photo" role="img" aria-label="Tilted amber spirit bottle with black labelled front"></div>

  <div class="intro-frame"></div>
  <div class="intro-card">
    <p>Hollowpine can bring your vision to life with our inhouse teams. We are here to help you through the entire process of creating unique spirit to compliment your brand.</p>
    <p>From formulating the recipe to production and even to helping you market your newest drink;</p>
  </div>

  <h2 class="about-title">ABOUT</h2>
  <div class="about-rule"></div>
  <div class="about-copy">
    <p>Hollowpine Spirits, located in the Netherlands, has been mixing creating 5-star-rated gin, cocktails and making recipes since 2017. Now we want to use our distilling expertise to help you launch your very own brand of liquor.</p>
    <p>Through our vast network we have exclusive access some of the best Whiskies, Vodka, Rum, Gins and Wines in the world.</p>
    <p>We work directly with you to develop the perfect recipe and produce your drink</p>
  </div>

  <footer class="footer">
    <div class="footer-brand"><span class="square"></span>HOLLOWPINE SPIRITS</div>
    <p class="footer-tagline">Turn your next drink idea into a reality and share your product with the world.</p>
    <div class="footer-divider"></div>
    <div class="contact-item" style="top:42px">
      <svg width="13" height="13" viewBox="0 0 24 24" fill="none" stroke="#c9a23a" stroke-width="2" stroke-linecap="round" stroke-linejoin="round"><path d="M22 16.9v3a2 2 0 0 1-2.2 2 19.8 19.8 0 0 1-8.6-3.1 19.5 19.5 0 0 1-6-6A19.8 19.8 0 0 1 2.1 4.2 2 2 0 0 1 4.1 2h3a2 2 0 0 1 2 1.7c.1 1 .4 1.9.7 2.8a2 2 0 0 1-.5 2.1L8 9.9a16 16 0 0 0 6 6l1.3-1.3a2 2 0 0 1 2.1-.4c.9.3 1.8.6 2.8.7a2 2 0 0 1 1.7 2z"/></svg>
      <span>+31655182047</span>
    </div>
    <div class="contact-item" style="top:83px">
      <svg width="13" height="14" viewBox="0 0 24 24" fill="none" stroke="#c9a23a" stroke-width="2" stroke-linecap="round" stroke-linejoin="round"><path d="M20 10c0 6-8 12-8 12S4 16 4 10a8 8 0 0 1 16 0z"/><circle cx="12" cy="10" r="3"/></svg>
      <span>Hollowpine Spirits Warehouse 14,<br>Duinweg Business Park, 8<br>Havenstraat,<br>Noordwijk, 2201KL</span>
    </div>
  </footer>
</body>
</html>
```